Breezeway Travel NI needs a new Website

We have an old website that is just that - old. We need a fresh website that is professional graphic designed that has the following features.
1. Can be updated by ourselves in some areas.
2. Has a shopping cart.
3. Has links to download PDF files
4. Has links to other pages in the website
5. Includes social media links
6. Has a client log-in area
Full details in brief provided.

SORRY BUT IT'S URGENT. We've taken too long to write the details and it is now urgent. So my apologies I will be asking for designers to work quickly.

We will continue to use our existing web hosting company and url. Their is a link to the old website in the Design Brief.
Updates

UPDATE:  Please see the new file UPDATE TO DESIGN BRIEF.
Thanks for all your submissions to date.  We hope the update will assist with your designs.
As indicated in previous messages, we are happy with the Home Page + 1 Page in order to select the designer to work with in creating the full design. 

Thankyou Designers.  Much appreciate your efforts.
It's getting late here on Norfolk so I won't have much chance too review any more designs this evening.
But for your information:
Designer 3817405 Ravindra Sethi is so far the closest to what we are seeking.
Thanks again. 

Reason: Have extended to Monday 7 October to give time for designers to submit after feedback today. Especially given the time differences

Target Market(s)

Very wide audience. Current client group not that tech savvy, but we hope to broaden our market and sell more creative products, and so website needs to consider how people now use media, ie tablets & iphones.

Industry/Entity Type

Shopping

Requirements
Nice to have
• PLEASE SEE THE "UPDATE TO THE DESIGN BRIEF"

```html
<!DOCTYPE html>
<html lang="en">
<head>
<meta charset="utf-8">
<title>Breezeway Travel NI – Home</title>
<link href="https://fonts.googleapis.com/css2?family=Ubuntu:wght@400;500&family=Dancing+Script:wght@400&display=swap" rel="stylesheet">
<style>
:root{
  --green:#0f9b48;
  --green-line:#0c8a3f;
  --orange:#ef7d1e;
  --orange-dark:#e06d10;
  --orange-soft:#f09a55;
  --navy:#16206e;
  --text:#666;
  --text-dark:#555;
  --rule:#dcdcdc;
  --paper:#f3f3f1;
  --side:#f4f4f4;
}
*{box-sizing:border-box;margin:0;padding:0}
html,body{width:1200px;height:1028px;overflow:hidden}
body{position:relative;background:var(--paper);font-family:"Ubuntu",sans-serif;color:var(--text)}
h1,h2,h3{font-weight:400}
.top-rule{position:absolute;left:0;top:0;width:1200px;height:5px;background:var(--green)}
.brand{position:absolute;left:475px;top:0;width:251px;height:102px;background:#fff;box-shadow:0 1px 3px rgba(0,0,0,.12);display:flex;align-items:center;justify-content:center;gap:10px}
.brand-dot{width:30px;height:30px;border-radius:50%;background:var(--orange)}
.brand-name{font-size:19px;font-weight:500;color:var(--orange);line-height:1.1;width:150px}
.page{position:absolute;left:75px;top:116px;width:1050px;height:861px;background:#fff;box-shadow:0 0 4px rgba(0,0,0,.08)}
.abs{position:absolute}

/* navigation */
.nav{position:absolute;left:0;top:0;width:215px;height:861px;background:var(--green)}
.nav a{display:flex;align-items:center;position:relative;height:36.6px;padding-left:41px;font-size:11.5px;line-height:18px;text-transform:uppercase;color:#fff;text-decoration:none;border-bottom:1px solid var(--green-line)}
.nav a.is-double{height:52px}
.nav a.is-tall{height:55px}
.nav a::before{content:"";position:absolute;left:24px;top:50%;margin-top:-4px;width:7px;height:7px;border:1px solid rgba(255,255,255,.7);border-radius:50%}
.nav a.is-double::before,.nav a.is-tall::before{top:16px;margin-top:0}
.nav a.is-current{background:var(--orange);height:41px}
.nav a.is-current::after{content:"";position:absolute;right:-6px;top:14px;border:6px solid transparent;border-left-color:var(--orange);border-right:0}

/* centre column */
.title{left:215px;width:573px;top:27px;text-align:center;font-family:"Dancing Script",cursive;font-size:42px;color:var(--orange);line-height:1}
.established{left:215px;width:573px;top:78px;text-align:center;font-size:12px;color:var(--orange-soft)}
.slider{left:239px;top:114px;width:528px;height:274px;background:linear-gradient(180deg,#7fb2d8 0%,#b9d5e6 22%,#3d6a3a 36%,#2f5a2e 52%,#4aa4b0 62%,#e5cfa5 78%,#d9b27e 100%)}
.slider-caption{position:absolute;left:0;top:190px;width:303px;height:60px;background:rgba(60,60,60,.72);clip-path:polygon(0 0,265px 0,100% 100%,0 100%);font-family:"Dancing Script",cursive;font-size:33px;color:#fff;padding:10px 0 0 22px}
.slider-arrow{position:absolute;top:128px;width:34px;height:30px}
.section-head{font-size:14px;line-height:16px;color:var(--orange)}
.rule{height:1px;background:var(--rule)}
.supports{left:239px;top:452px;width:522px;height:99px;display:flex}
.support{display:flex;flex-direction:column;align-items:center;justify-content:center;gap:12px;font-size:14px;color:var(--text-dark)}
.support.is-active{background:var(--orange);color:#fff}
.support-sep{width:1px;background:var(--rule);margin:8px 0}
.events{left:239px;top:608px;width:520px;height:105px;background:#f5f5f5;border:1px solid #e6e6e6}
.event{position:absolute;top:20px;width:210px;font-size:11px;line-height:16px;color:var(--text)}
.event h3{font-size:13px;line-height:16px;color:var(--green);margin-bottom:4px}
.event svg{position:absolute;left:-39px;top:2px}
.banner{left:240px;top:731px;width:519px;height:104px;background:linear-gradient(180deg,#4f9fd2 0%,#8cc6e6 30%,#20b6c4 55%,#55c7c9 75%,#d9c79a 100%);overflow:hidden}
.banner-people{position:absolute;right:0;top:0;width:178px;height:104px;background:linear-gradient(135deg,#8a7a58,#6b5a45 60%,#a49776)}
.banner-title{position:absolute;left:17px;top:20px;font-size:20.5px;color:#fff;text-shadow:0 1px 2px rgba(0,0,0,.35);white-space:nowrap}
.btn-book{position:absolute;left:18px;top:67px;width:123px;height:25px;background:var(--orange);border:1px solid #f6a55c;color:#fff;font-size:13px;text-align:center;line-height:23px}

/* right column */
.aside{position:absolute;left:788px;top:0;width:262px;height:861px;background:var(--side)}
.side-head{font-size:13px;line-height:15px;color:var(--orange)}
.side-text{font-size:11px;line-height:16px;color:var(--text)}
.video{left:832px;top:424px;width:184px;height:86px;background:linear-gradient(180deg,#87b6d8 0%,#3e6b3c 35%,#2fa4b3 60%,#e3caa0 100%)}
.play{position:absolute;left:71px;top:22px;width:42px;height:42px;border-radius:50%;background:var(--orange);border:3px solid #fff}
.play::after{content:"";position:absolute;left:14px;top:9px;border:9px solid transparent;border-left:13px solid #fff;border-right:0}
.btn-social{left:834px;top:567px;width:181px;height:36px;background:var(--navy);color:#fff;font-size:16px;display:flex;align-items:center}
.btn-social .sq{width:10px;height:10px;background:#fff;margin:0 22px 0 16px}
.btn-login{left:833px;top:616px;width:108px;height:26px;background:var(--green);color:#fff;font-size:11px;display:flex;align-items:center;justify-content:center;gap:6px}
.support-center{left:813px;top:690px;width:205px;height:85px;background:linear-gradient(90deg,#2f6fa5 0%,#6ca3c9 55%,#c9d9e6 100%);font-size:17px;font-weight:500;color:#fff;line-height:20px;padding:22px 0 0 18px}
.btn-shop{left:814px;top:789px;width:204px;height:35px;background:var(--orange);color:#fff;font-size:18px;font-weight:500;text-align:center;line-height:33px;border:1px solid var(--orange-dark)}
</style>
</head>
<body>
<div class="top-rule"></div>
<header class="brand"><span class="brand-dot"></span><span class="brand-name">Breezeway Travel NI</span></header>

<main class="page">
  <nav class="nav">
    <a class="is-current">Home</a>
    <a>Governance</a>
    <a>Norfolk Island</a>
    <a>Our Mission &amp; Values</a>
    <a>Services</a>
    <a>Our Facilitators</a>
    <a>Our Shop</a>
    <a>Holiday Programs</a>
    <a class="is-double">Design Your Own<br>Norfolk Island Holiday</a>
    <a>DDD Creative Projects</a>
    <a class="is-tall">Schoolies, Siblings &amp;<br>Family Holidays</a>
    <a>Make a Booking</a>
    <a>Testimonials</a>
  </nav>

  <aside class="aside"></aside>

  <h1 class="abs title">Our Social Enterprise</h1>
  <p class="abs established">Established July 2001</p>

  <section class="abs slider" role="img" aria-label="Photo of a couple walking along a sandy Norfolk Island beach lined with pine trees">
    <svg class="slider-arrow" style="left:0" viewBox="0 0 34 30"><path d="M21 8 12 15l9 7z" fill="#fff"/></svg>
    <svg class="slider-arrow" style="right:0;background:rgba(255,255,255,.25)" viewBox="0 0 34 30"><path d="M13 8l9 7-9 7z" fill="#fff"/></svg>
    <div class="slider-caption">Norfolk Island</div>
  </section>

  <h2 class="abs section-head" style="left:239px;top:418px">We Support In</h2>
  <div class="abs rule" style="left:239px;top:441px;width:556px"></div>

  <div class="abs supports">
    <div class="support" style="width:110px"><svg width="34" height="30" viewBox="0 0 34 30"><rect x="2" y="6" width="24" height="20" fill="none" stroke="#999" stroke-width="2"/><rect x="8" y="2" width="24" height="20" fill="#fff" stroke="#999" stroke-width="2"/><path d="M11 19l6-7 4 4 3-3 5 6z" fill="#999"/></svg>Holidays</div>
    <div class="support-sep"></div>
    <div class="support" style="width:95px"><svg width="32" height="30" viewBox="0 0 32 30"><rect x="5" y="2" width="22" height="22" rx="4" fill="#999"/><rect x="8" y="7" width="16" height="8" fill="#fff"/><circle cx="10" cy="20" r="2" fill="#fff"/><circle cx="22" cy="20" r="2" fill="#fff"/><rect x="7" y="24" width="4" height="4" fill="#999"/><rect x="21" y="24" width="4" height="4" fill="#999"/></svg>Travel</div>
    <div class="support is-active" style="width:112px"><svg width="32" height="26" viewBox="0 0 32 26"><path d="M5 14V8h18V4l6 6-6 6v-4H9v2zM27 12v6H9v4l-6-6 6-6v4h14v-2z" fill="#fff"/></svg>Recreation</div>
    <div class="support" style="width:102px"><svg width="30" height="28" viewBox="0 0 30 28"><path d="M15 27S2 18 2 9a7 7 0 0 1 13-4 7 7 0 0 1 13 4c0 9-13 18-13 18z" fill="#999"/></svg>Respite</div>
    <div class="support-sep"></div>
    <div class="support" style="width:101px"><svg width="30" height="28" viewBox="0 0 30 28"><rect x="2" y="7" width="26" height="19" rx="2" fill="#999"/><rect x="10" y="2" width="10" height="6" fill="none" stroke="#999" stroke-width="2"/><rect x="12" y="14" width="6" height="4" fill="#fff"/></svg>Projects</div>
  </div>
  <div class="abs rule" style="left:239px;top:561px;width:556px"></div>

  <h2 class="abs section-head" style="left:239px;top:587px">Socially Inclusive Events</h2>
  <section class="abs events">
    <div class="event" style="left:62px">
      <svg width="28" height="28" viewBox="0 0 28 28"><rect x="2" y="5" width="24" height="21" fill="none" stroke="#999" stroke-width="2"/><rect x="2" y="5" width="24" height="5" fill="#999"/><rect x="7" y="1" width="3" height="7" fill="#999"/><rect x="18" y="1" width="3" height="7" fill="#999"/><text x="14" y="22" font-size="9" text-anchor="middle" fill="#888" font-family="Ubuntu,sans-serif">23</text></svg>
      <h3>Intellectual Disability</h3>Sodales ac ultrices! Modi,<br>hendrerit. Dis eos metus pulvinar.
    </div>
    <div class="event" style="left:338px">
      <svg width="28" height="28" viewBox="0 0 28 28"><rect x="2" y="5" width="24" height="21" fill="none" stroke="#999" stroke-width="2"/><rect x="2" y="5" width="24" height="5" fill="#999"/><rect x="7" y="1" width="3" height="7" fill="#999"/><rect x="18" y="1" width="3" height="7" fill="#999"/><text x="14" y="22" font-size="9" text-anchor="middle" fill="#888" font-family="Ubuntu,sans-serif">23</text></svg>
      <h3>Acquired Brain Injury</h3>Sodales ac ultrices! Modi,<br>hendrerit. Dis eos metus pulvinar.
    </div>
  </section>

  <section class="abs banner" role="img" aria-label="Photo of a turquoise lagoon with two smiling family members">
    <div class="banner-people"></div>
    <div class="banner-title">Siblings of children with Disabilities</div>
    <div class="btn-book">Book Now!</div>
  </section>

  <!-- right column content, page coordinates -->
  <h2 class="abs side-head" style="left:811px;top:35px;font-size:12.5px">LOCATION &amp; CONTACTS</h2>
  <div class="abs rule" style="left:811px;top:48px;width:227px;height:2px"></div>
  <svg class="abs" style="left:813px;top:65px" width="12" height="16" viewBox="0 0 12 16"><path d="M6 16S0 9 0 6a6 6 0 0 1 12 0c0 3-6 10-6 10z" fill="#aaa"/><circle cx="6" cy="6" r="2" fill="#f4f4f4"/></svg>
  <p class="abs side-text" style="left:832px;top:62px">Hibiscus Lane, Cascade Hill<br>PO Box 514<br>Norfolk Island NSW 2899<br>SOUTH PACIFIC<br>N.B.N. 417 602 358</p>

  <h2 class="abs side-head" style="left:811px;top:165px">Telephone</h2>
  <div class="abs rule" style="left:811px;top:183px;width:220px"></div>
  <svg class="abs" style="left:813px;top:199px" width="11" height="15" viewBox="0 0 11 15"><rect x="0" y="0" width="11" height="15" rx="1" fill="#aaa"/><rect x="2" y="2" width="7" height="4" fill="#f4f4f4"/></svg>
  <p class="abs side-text" style="left:832px;top:197px">International + 67 23 51907<br>Australia 1800 463 218<br>New Zealand</p>

  <h2 class="abs side-head" style="left:811px;top:274px">Email &nbsp;Website &amp; &nbsp;Friendbook</h2>
  <div class="abs rule" style="left:811px;top:292px;width:220px"></div>
  <svg class="abs" style="left:811px;top:308px" width="14" height="10" viewBox="0 0 14 10"><rect width="14" height="10" fill="#aaa"/><path d="M0 0l7 6 7-6" fill="none" stroke="#f4f4f4" stroke-width="1.2"/></svg>
  <p class="abs side-text" style="left:832px;top:305px">hello@breezewaytravel.org<br>www.breezewaytravel.org<br>www.friendbook.com/breezewaytravel</p>

  <h2 class="abs side-head" style="left:811px;top:373px">Images &amp; Video</h2>
  <div class="abs rule" style="left:811px;top:391px;width:220px"></div>
  <svg class="abs" style="left:809px;top:403px" width="16" height="14" viewBox="0 0 16 14"><circle cx="4" cy="3" r="3" fill="#aaa"/><circle cx="10" cy="3" r="3" fill="#aaa"/><rect x="1" y="6" width="11" height="7" fill="#aaa"/><path d="M12 8l4-2v7l-4-2z" fill="#aaa"/></svg>
  <p class="abs side-text" style="left:832px;top:403px;font-size:10.5px">BREEZY HOLS VIDEO</p>

  <div class="abs video" role="img" aria-label="Video still of a Norfolk Island beach"><span class="play"></span></div>
  <p class="abs side-text" style="left:832px;top:531px;font-size:9.5px;line-height:14px">to see more photographs and video's<br>LIKE our FRIENDBOOK page</p>
  <div class="abs btn-social"><span class="sq"></span>Go to Friendbook</div>
  <div class="abs btn-login"><svg width="8" height="10" viewBox="0 0 8 10"><rect y="4" width="8" height="6" fill="#fff"/><path d="M2 4V3a2 2 0 0 1 4 0v1" fill="none" stroke="#fff" stroke-width="1.3"/></svg>CLIENT LOGIN</div>
  <svg class="abs" style="left:956px;top:624px" width="30" height="10" viewBox="0 0 30 10"><path d="M0 5h27M24 2l3 3-3 3" fill="none" stroke="#ccc"/></svg>
  <svg class="abs" style="left:1001px;top:620px" width="16" height="17" viewBox="0 0 16 17"><circle cx="8" cy="5" r="4" fill="#aaa"/><path d="M0 17c0-5 3-7 8-7s8 2 8 7z" fill="#aaa"/></svg>

  <h2 class="abs side-head" style="left:811px;top:671px">Support Us</h2>
  <div class="abs support-center" role="img" aria-label="Photo of a support agent wearing a headset">Support<br>Center</div>
  <div class="abs btn-shop">OUR SHOP</div>
</main>
</body>
</html>
```